Design New Business Card, Envelope and Letter Head !

We need a stationery design for our newly developed logo! We need professional classic look.

Front of the Card:
Logo on the left hand side

Personal Detail in the right hand side
i.e. Name,
Title
Office:
Cell:
Fax:
email:

www.torvanlending.example

Color Scheme should match our logo.

Back Side of the Card:

Logo again with Green back ground or off gray back ground ( Note: Color has to be from logo)

and below message. Again, font size and color should come from logo.

" Manifest your trust in us through the gift of your referrals. We won't let you down."
Updates

Dear Designers;

We have updates few info which we missed earlier. Please include those words in the logo and resubmit your designs for consideration.  We are looking for very professional and classic look. Thanks for your great creation. I have changed the payment options. Please have a look and best of luck.

Ned

Dear All Designers:

For address; please use following address:

" 4172 Willow Crest Ln, Alder Bay, WA 98999 " 
Please do not use the address in the website. We would like to give business card with option of calling us is the top priority then email then qLine. Please make sure Put " qLine" in the business card. 

Reason: Since I have updated some information per requirements, I would like to give enough time for the great design work.

Just a note to all designers:

"Equal Opportunity Lender" Sign has to be in back  of the card  in a small image. I would say it has to be "inconspicuous". Let's put the HRQA # and StaPLO # in front side. Let's organise the information follow very elegant and professional.

Requirements
Must have
• We must need following Words in the business card

StaPLO License #

HRQA #

And the logo of " Equal Housing Lender ". Please see the logo attached.

Please put these words or logo represents above at the right location of the card.

```html
<!DOCTYPE html>
<html lang="en">
<head>
<meta charset="utf-8">
<title>Torvan Lending Stationery</title>
<link href="https://fonts.googleapis.com/css2?family=Open+Sans:ital,wght@0,400;0,600;0,700;1,700&family=Dancing+Script&display=swap" rel="stylesheet">
<style>
:root{
  --green:#4b9534;
  --dark:#3f3f3f;
  --ink:#333333;
  --paper:#f3f3f3;
  --bg:#e9e9e9;
  --muted:#666666;
}
*{box-sizing:border-box;margin:0;padding:0}
html,body{width:1200px;height:1000px;overflow:hidden}
body{background:var(--bg);font-family:"Open Sans",Arial,sans-serif;color:var(--ink);position:relative}
.sheet{position:absolute;background:var(--paper)}
.brand{display:flex;align-items:center;gap:5px;font-family:"Open Sans",Arial,sans-serif;font-weight:600;color:var(--dark);white-space:nowrap}
.brand-mark{background:var(--green);flex:none}
.bar-dark,.bar-green{position:absolute;bottom:0}
.bar-dark{background:var(--dark)}
.bar-green{background:var(--green)}
.corner-mark{position:absolute;background:var(--green)}
.dot{display:inline-block;width:4px;height:4px;border-radius:50%;background:var(--green);margin-right:2px;vertical-align:middle}

/* letterhead */
.letterhead{left:212px;top:125px;width:341px;height:522px}
.letterhead .brand{position:absolute;left:60px;top:58px;font-size:13px}
.letterhead .brand-mark{width:10px;height:10px}
.letter-headline{position:absolute;right:33px;top:115px;font-size:8.5px;font-weight:700;font-style:italic;color:var(--green)}
.letter-body{position:absolute;left:60px;top:137px;width:249px;font-size:6px;line-height:8.3px;color:var(--ink)}
.letter-body p{margin-bottom:9px;text-align:justify}
.letter-body .gap{margin-bottom:17px}
.signature{position:absolute;right:33px;top:420px;font-family:"Dancing Script",cursive;font-size:16px;color:var(--ink)}
.letter-contact{position:absolute;left:18px;top:494px;font-size:5.3px;line-height:8px;color:var(--ink)}
.letter-contact .row{display:flex;gap:6px;white-space:nowrap}
.letter-contact .row.addr{padding-left:55px}
.letterhead .bar-dark{left:0;width:266px;height:6px}
.letterhead .bar-green{left:269px;width:72px;height:6px}
.letterhead .corner-mark{left:312px;top:496px;width:12px;height:12px}

/* folder */
.folder{left:645px;top:100px;width:435px;height:550px}
.folder .brand{position:absolute;left:75px;top:205px;font-size:27px;gap:10px}
.folder .brand-mark{width:20px;height:20px}
.folder .bar-dark{left:0;width:314px;height:8px}
.folder .bar-green{left:317px;width:118px;height:8px}
.folder .corner-mark{left:370px;top:518px;width:14px;height:14px}

/* business cards */
.card{width:167px;height:94px}
.card-back{left:80px;top:692px;background:var(--green)}
.card-back .brand{position:absolute;left:30px;top:28px;font-size:11px;color:#ffffff}
.card-back .brand-mark{width:8px;height:8px;background:#ffffff}
.card-message{position:absolute;left:40px;top:48px;width:118px;font-size:4px;line-height:5.5px;color:#ffffff;text-align:center}
.card-back .badge{position:absolute;right:8px;bottom:7px;width:8px;height:8px;border:1px solid #ffffff}
.card-front{left:80px;top:814px}
.card-front .brand{position:absolute;left:8px;top:34px;font-size:7.5px}
.card-front .brand-mark{width:5px;height:5px}
.card-name{position:absolute;left:97px;top:21px;font-size:11px;color:var(--dark)}
.card-title{position:absolute;left:98px;top:35px;font-size:4.5px;color:var(--green)}
.card-details{position:absolute;left:97px;top:46px;font-size:3.8px;line-height:5px;color:var(--ink)}
.card-license{position:absolute;left:22px;top:80px;font-size:3px;line-height:4px;color:var(--muted)}
.card-front .eq-badge{position:absolute;left:7px;top:72px;width:11px;height:11px;background:var(--dark)}
.card-front .bar-dark{left:0;width:120px;height:3px}
.card-front .bar-green{left:122px;width:45px;height:3px}

/* envelopes */
.envelope{width:413px;height:197px}
.envelope-front{left:290px;top:707px}
.envelope-front .brand{position:absolute;left:12px;top:162px;font-size:14px}
.envelope-front .brand-mark{width:10px;height:10px}
.envelope-front .bar-dark{left:0;width:298px;height:6px}
.envelope-front .bar-green{left:302px;width:111px;height:6px}
.envelope-front .corner-mark{left:350px;top:172px;width:12px;height:12px}
.envelope-back{left:742px;top:707px;width:415px}
.flap{position:absolute;left:0;top:0;width:100%;height:41px;background:var(--green)}
.envelope-back .brand{position:absolute;left:290px;top:127px;font-size:11px}
.envelope-back .brand-mark{width:8px;height:8px}
.envelope-contact{position:absolute;left:298px;top:146px;font-size:5.5px;line-height:7.7px;color:var(--ink)}
</style>
</head>
<body>

<section class="sheet letterhead" aria-label="Letterhead">
  <div class="brand"><span class="brand-mark"></span>Torvan Lending</div>
  <p class="letter-headline">Lorem ipsum dolor sit ametconsectetur.</p>
  <div class="letter-body">
    <p>Dear Parent,</p>
    <p class="gap">Lorem ipsum dolor sit amet, consectetur adipiscing elit. Nulla sodales nisi vitae Lorem ipsum dolor sit amet, consectetur adipiscing elit. Suspendisse feugiat eros nisl, a facilisis risus eleifend sed. Aliquam mauris enim, fermentum eu lacinia sit amet, laoreet eu leo. Nullam eleifend nulla in libero tristique, ac vulputate odio tincidunt. Etiam non condimentum tortor. Integer suscipit neque nec odio porttitor cursus. Phasellus a sapien blandit, suscipit justo id, condimentum ante. Morbi tristique justo risus, id mattis dui molestie ut. Nullam volutpat ut quam commodo faucibus. Pellentesque urna est, interdum in elit quis, pharetra elementum orci. Nam pharetra velit molestie justo placerat scelerisque.</p>
    <p class="gap">Nulla tincidunt molestie libero vel pretium. Donec condimentum nulla sit amet risus semper imperdiet. Duis congue eros nec diam blandit, et pellentesque sapien auctor. Curabitur iaculis enim lectus, in imperdiet mauris mattis eget. Etiam ac ornare metus. Mauris risus leo, egestas at dolor a, ultrices adipiscing est. Nunc faucibus scelerisque mollis. Pellentesque aliquet mauris tellus, id dignissim risus viverra et. Mauris venenatis lobortis eros. Nam id diam in ligula malesuada feugiat. Cras turpis felis, aliquet id mauris elementum, feugiat ultricies nisl.</p>
    <p class="gap">Nullam auctor venenatis metus, eu pulvinar sapien dapibus non. Cum sociis natoque penatibus et magnis dis parturient montes, nascetur ridiculus mus. Praesent sed lorem eget tortor volutpat dictum vel vel ipsum. Morbi ac mauris sed elit dictum volutpat. Morbi pulvinar non nisi in ultrices. Pellentesque quis mi in risus eleifend adipiscing.</p>
    <p>Best regards.</p>
  </div>
  <p class="signature">Mark Ellison</p>
  <div class="letter-contact">
    <div class="row addr"><span><span class="dot"></span>4172 Willow Crest Ln, Alder Bay, WA 98999</span></div>
    <div class="row">
      <span><span class="dot"></span>(555) 555-0140</span>
      <span><span class="dot"></span>(555) 555-0163</span>
      <span><span class="dot"></span>info@torvanlending.example</span>
      <span><span class="dot"></span>www.torvanlending.example</span>
    </div>
  </div>
  <span class="corner-mark"></span>
  <span class="bar-dark"></span><span class="bar-green"></span>
</section>

<section class="sheet folder" aria-label="Presentation folder">
  <div class="brand"><span class="brand-mark"></span>Torvan Lending</div>
  <span class="corner-mark"></span>
  <span class="bar-dark"></span><span class="bar-green"></span>
</section>

<section class="sheet card card-back" aria-label="Business card back">
  <div class="brand"><span class="brand-mark"></span>Torvan Lending</div>
  <p class="card-message">"Manifest your trust in us through the gift of your referrals.<br>We won't let you down."</p>
  <span class="badge"></span>
</section>

<section class="sheet card card-front" aria-label="Business card front">
  <div class="brand"><span class="brand-mark"></span>Torvan Lending</div>
  <p class="card-name">Mark Ellison</p>
  <p class="card-title">Chief Executive Officer</p>
  <div class="card-details">
    <div><span class="dot"></span>4172 Willow Crest Ln,</div>
    <div>&nbsp;&nbsp;Alder Bay, WA 98999</div>
    <div><span class="dot"></span>Office: (555) 555-0140</div>
    <div><span class="dot"></span>info@torvanlending.example</div>
    <div><span class="dot"></span>qLine: (555) 555-0163</div>
    <div><span class="dot"></span>www.torvanlending.example</div>
  </div>
  <span class="eq-badge"></span>
  <div class="card-license">
    <div>StaPLO License # 01234567</div>
    <div>HRQA # 1234567</div>
  </div>
  <span class="bar-dark"></span><span class="bar-green"></span>
</section>

<section class="sheet envelope envelope-front" aria-label="Envelope front">
  <div class="brand"><span class="brand-mark"></span>Torvan Lending</div>
  <span class="corner-mark"></span>
  <span class="bar-dark"></span><span class="bar-green"></span>
</section>

<section class="sheet envelope envelope-back" aria-label="Envelope back">
  <span class="flap"></span>
  <div class="brand"><span class="brand-mark"></span>Torvan Lending</div>
  <div class="envelope-contact">
    <div><span class="dot"></span>4172 Willow Crest Ln,</div>
    <div>&nbsp;&nbsp;Alder Bay, WA 98999</div>
    <div><span class="dot"></span>(555) 555-0140</div>
    <div><span class="dot"></span>info@torvanlending.example</div>
    <div><span class="dot"></span>(555) 555-0163</div>
    <div><span class="dot"></span>www.torvanlending.example</div>
  </div>
</section>

</body>
</html>
```